Business card design needed

Beauty salon
I have an Art Nouveau theme. I would like an ornate frame, my salon name 'Velvet Harbour Beauty' written is some kind of elegant, vintage, art deco font. I saw two fonts online that I thought were ok - Andes and Art Nouveau Caps. But I am open to new fonts. I would also like to add a picture of a woman from that era if possible. I want the front of the business card to look like a vintage, art nouveau advertisment poster.
Then on the back I would like address (Shop 4, 15-31 Kellaway Rd Brimfield VIC 3194), contact number (0412 638 207), email address (info@velvetharbour.com.au) and website address (www.velvetharbour.com.au).
The words "your next appointment _______________________" I would also like.
I would like this to be in a more traditional, easy to read, basic font.
I would like the business card to be vertical, not horizontal.

Target Market(s)
Females aged 18-60
Industry/Entity Type
Salon
Contact Information for Business Card
Image on front (full size)
Text on back - Velvet Harbour Beauty, Shop 4 15-31 Kellaway Rd Brimfield, 0412638207, www.velvetharbour.com.au
Your next appointment ___________________________

```html
<!DOCTYPE html>
<html lang="en">
<head>
<meta charset="utf-8">
<title>Velvet Harbour Beauty – Business Cards</title>
<link rel="stylesheet" href="https://fonts.googleapis.com/css2?family=Federo&family=Open+Sans:wght@400;700&display=swap">
<style>
  :root {
    --page: #ffffff;
    --page-edge: #e4e4e4;
    --cream: #fdfde0;
    --forest: #225a2a;
    --sage: #4f7d55;
    --white: #ffffff;
    --ink: #222222;
  }
  html, body {
    margin: 0;
    padding: 0;
    overflow: hidden;
    background: var(--page);
  }
  .canvas {
    position: relative;
    width: 1200px;
    height: 660px;
    box-sizing: border-box;
    border: 1px solid var(--page-edge);
    background: var(--page);
    overflow: hidden;
  }
  .symbols { position: absolute; width: 0; height: 0; }

  .card {
    position: absolute;
    top: 53px;
    width: 310px;
    height: 535px;
    box-sizing: border-box;
    overflow: hidden;
  }
  .card--front-light { left: 76px; background: var(--cream); color: var(--sage); }
  .card--front-dark  { left: 454px; background: var(--forest); border-radius: 18px; color: var(--white); }
  .card--back        { left: 796px; background: var(--forest); border-radius: 18px; color: var(--white); }

  .card__frame {
    position: absolute;
    left: 0;
    top: 0;
    width: 310px;
    height: 535px;
  }

  .portrait {
    position: absolute;
    border-radius: 48% 42% 30% 55% / 22% 26% 60% 58%;
  }
  .card--front-light .portrait {
    left: 78px;
    top: 85px;
    width: 150px;
    height: 290px;
    background: linear-gradient(170deg, #5e8a63, #4f7d55 60%, #6d9472);
  }
  .card--front-dark .portrait {
    left: 74px;
    top: 58px;
    width: 158px;
    height: 298px;
    background: linear-gradient(170deg, #ffffff, #e7efe6 70%, #f4f7f2);
  }
  .card--back .portrait--faint {
    left: 76px;
    top: 58px;
    width: 158px;
    height: 298px;
    background: linear-gradient(170deg, rgba(255,255,255,0.14), rgba(255,255,255,0.07));
  }

  .salon-name {
    position: absolute;
    left: 0;
    right: 0;
    margin: 0;
    text-align: center;
    font-family: "Federo", serif;
    font-weight: 400;
    text-transform: uppercase;
    letter-spacing: 3px;
  }
  .card--front-light .salon-name { top: 388px; font-size: 26px; line-height: 34px; color: var(--sage); }
  .card--front-dark .salon-name { top: 364px; font-size: 30px; line-height: 42px; color: var(--white); }

  .contact {
    position: absolute;
    inset: 0;
    font-family: "Open Sans", Arial, sans-serif;
    font-weight: 700;
    color: var(--white);
    text-align: center;
  }
  .contact p { position: absolute; left: 0; right: 0; margin: 0; }
  .contact__name { top: 87px; font-size: 17px; }
  .contact__address { top: 135px; font-size: 15px; line-height: 21px; }
  .contact__phone { top: 212px; font-size: 15px; display: flex; justify-content: center; align-items: center; gap: 6px; }
  .contact__phone svg { width: 14px; height: 14px; }
  .contact__email { top: 296px; font-size: 13px; }
  .contact__web { top: 319px; font-size: 13px; }

  .appointment {
    position: absolute;
    left: 41px;
    top: 372px;
    width: 223px;
    height: 117px;
    background: var(--white);
    border-radius: 14px;
    font-family: "Open Sans", Arial, sans-serif;
    color: var(--ink);
  }
  .appointment__label {
    margin: 0;
    position: absolute;
    top: 13px;
    left: 0;
    right: 0;
    text-align: center;
    font-size: 14px;
  }
  .appointment__line {
    position: absolute;
    left: 30px;
    width: 168px;
    border-top: 1px solid var(--ink);
  }
  .appointment__line--first { top: 59px; }
  .appointment__line--second { top: 92px; }
</style>
</head>
<body>
<main class="canvas">

  <svg class="symbols" aria-hidden="true">
    <defs>
      <symbol id="card-frame" viewBox="0 0 310 535">
        <g fill="none" stroke="currentColor" stroke-linecap="round">
          <!-- top arched bands -->
          <path d="M24 22 Q155 4 286 22" stroke-width="4"/>
          <path d="M30 30 Q155 14 280 30" stroke-width="1.5"/>
          <!-- side rails with gentle curves -->
          <path d="M18 40 C12 130 26 200 19 268 C12 340 26 420 18 500" stroke-width="3.5"/>
          <path d="M292 40 C298 130 284 200 291 268 C298 340 284 420 292 500" stroke-width="3.5"/>
          <path d="M26 50 C22 140 30 200 27 268 C24 340 30 420 26 490" stroke-width="1.2"/>
          <path d="M284 50 C288 140 280 200 283 268 C286 340 280 420 284 490" stroke-width="1.2"/>
          <!-- side brackets -->
          <path d="M19 150 q9 -8 16 0 M19 268 q9 -8 16 0 M19 390 q9 -8 16 0" stroke-width="2"/>
          <path d="M291 150 q-9 -8 -16 0 M291 268 q-9 -8 -16 0 M291 390 q-9 -8 -16 0" stroke-width="2"/>
          <!-- corner curls -->
          <path d="M18 40 Q18 22 34 20" stroke-width="3"/>
          <path d="M292 40 Q292 22 276 20" stroke-width="3"/>
          <path d="M18 500 Q20 516 36 514" stroke-width="3"/>
          <path d="M292 500 Q290 516 274 514" stroke-width="3"/>
          <!-- bottom bands -->
          <path d="M30 508 Q155 490 280 508" stroke-width="1.5"/>
          <path d="M20 516 L290 516" stroke-width="4"/>
          <path d="M24 524 L286 524" stroke-width="1.5"/>
        </g>
        <g fill="currentColor">
          <circle cx="12" cy="30" r="2.2"/>
          <circle cx="12" cy="42" r="1.8"/>
          <circle cx="298" cy="30" r="2.2"/>
          <circle cx="298" cy="42" r="1.8"/>
          <circle cx="155" cy="11" r="2.5"/>
        </g>
      </symbol>
    </defs>
  </svg>

  <section class="card card--front-light" aria-label="Front of card, light version">
    <svg class="card__frame" aria-hidden="true"><use href="#card-frame"/></svg>
    <div class="portrait" role="img" aria-label="Art Nouveau illustration of a woman in profile with long flowing hair, in sage green"></div>
    <h1 class="salon-name">Velvet<br>Harbour<br>Beauty</h1>
  </section>

  <section class="card card--front-dark" aria-label="Front of card, dark version">
    <svg class="card__frame" aria-hidden="true"><use href="#card-frame"/></svg>
    <div class="portrait" role="img" aria-label="Art Nouveau illustration of a woman in profile with long flowing hair, in white"></div>
    <h2 class="salon-name">Velvet<br>Harbour<br>Beauty</h2>
  </section>

  <section class="card card--back" aria-label="Back of card">
    <svg class="card__frame" aria-hidden="true"><use href="#card-frame"/></svg>
    <div class="portrait portrait--faint" role="img" aria-label="Faint Art Nouveau illustration of a woman behind the contact details"></div>
    <div class="contact">
      <p class="contact__name">Velvet Harbour Beauty</p>
      <p class="contact__address">Shop 4 15-31<br>Kellaway Rd Brimfield</p>
      <p class="contact__phone">
        <svg viewBox="0 0 24 24" aria-hidden="true"><path fill="currentColor" d="M6.6 10.8a15.1 15.1 0 0 0 6.6 6.6l2.2-2.2a1 1 0 0 1 1-.25 11.4 11.4 0 0 0 3.6.57 1 1 0 0 1 1 1V20a1 1 0 0 1-1 1A17 17 0 0 1 3 4a1 1 0 0 1 1-1h3.5a1 1 0 0 1 1 1c0 1.25.2 2.45.57 3.57a1 1 0 0 1-.25 1z"/></svg>
        0412638207
      </p>
      <p class="contact__email">info@velvetharbour.com.au</p>
      <p class="contact__web">www.velvetharbour.com.au</p>
    </div>
    <div class="appointment">
      <p class="appointment__label">Your next appointment:</p>
      <div class="appointment__line appointment__line--first"></div>
      <div class="appointment__line appointment__line--second"></div>
    </div>
  </section>

</main>
</body>
</html>
```